Home page design layout for commercial driving school

- This is for a layout design of the home page only. No coding required.

- The design must be based around the attached HPID (home page information design). The table boxes are just for approximate placement of information – you DON'T have to make it look exactly like this. Information only is in orange text. Copy to go on the design in black text. Some instructions are in the HPID. Please be creative! You don’t have to use the exact images provided if you have a better idea.

- The design needs to be professional and modern. Fonts used except in the header must be Google fonts.

I've attached:
- HPID (information design) as a Word doc and PDF
- the logo. Please use the colours from the logos in the website design. Lots of white too.
- images for the gallery
- icon examples for the buttons for under the gallery - these aren't high resolution. If you have access to better examples please use those instead.
- logos of accreditations for that section
- background image that you may or may not use. This image is used in the business folders and business cards and I've got an example in this folder. If you can incorporate this into the design you may but it's not compulsory.

The winning PSD file will have to be provided as follows…
1. Canvas size of 2000px x 2000px - 72ppi in Adobe Photoshop (CS5 compatible)
2. Width of content section is 1100px wide - centered in the canvas
3. Header height (without nav bar) 150-160 pixels.
4. Any button rollovers/hovers in the PSD as hidden layers.
5. All fonts used must be Google fonts (except for the header fonts).
6. You will need to supply the chosen home page plus one example page (example page as a style guide for how all other pages will look). Example page is only the header and navigational bar at the top, an empty sector in the middle with a column (180 px wide) which can be left or right aligned which means the main sector is 920 pixels wide, and then the footer at the bottom of the page.

Apologies for the delay in assigning a first place for this project. We will be completing this project as soon as we can.

```html
<!DOCTYPE html>
<html lang="en">
<head>
<meta charset="utf-8">
<title>Steerwell Driver Training – Home</title>
<link href="https://fonts.googleapis.com/css2?family=Open+Sans:wght@400;600&display=swap" rel="stylesheet">
<style>
:root{
  --blue:#3f73bd;
  --tile:#4a7bc4;
  --nav:#a3dd94;
  --nav-active:#5cc256;
  --panel:#e4e4e4;
  --text:#555;
  --muted:#777;
  --rule:#cfcfcf;
}
*{box-sizing:border-box;margin:0;padding:0}
html,body{width:1200px;height:1200px;overflow:hidden}
body{position:relative;font-family:"Open Sans",sans-serif;color:var(--text);background:#fff}
.backdrop{position:absolute;top:0;width:270px;height:1200px;background:linear-gradient(180deg,#1d3f9a 0%,#4f73c8 14%,#a9bde8 24%,#f4f7fd 32%,#fff 45%)}
.backdrop.left{left:0}.backdrop.right{right:0}
.page{position:absolute;left:270px;top:0;width:660px;height:1200px;background:#fff;box-shadow:0 0 4px rgba(0,0,0,.25)}
.abs{position:absolute}
/* header */
.brand{left:6px;top:6px;width:92px;height:84px;display:flex;flex-direction:column;align-items:center;justify-content:center;gap:4px}
.brand-mark{width:38px;height:38px;border-radius:50%;background:var(--blue)}
.brand-name{font-size:10px;font-weight:600;color:var(--blue);text-align:center;line-height:1.15}
.coverage{left:102px;top:0;width:160px;height:96px;border-left:1px solid #ddd;border-right:1px solid #ddd}
.coverage .title{position:absolute;left:6px;top:8px;font:11px Arial,sans-serif;color:#222;white-space:nowrap}
.coverage .map{position:absolute;left:6px;top:26px;width:56px;height:64px;background:linear-gradient(135deg,#9fdc7a,#6cc04a)}
.coverage .office{position:absolute;left:66px;top:54px;font:9px/1.25 Arial,sans-serif;color:#222}
.tagline{left:266px;width:386px;top:18px;text-align:right;font-family:Arial,sans-serif;color:#222}
.tagline h1{font-size:14px;font-weight:normal;margin-bottom:4px;white-space:nowrap}
.tagline p{font-size:8.6px;line-height:1.65;white-space:nowrap}
.tagline em{font-size:10px}
/* nav */
.nav{left:0;top:96px;width:660px;height:24px;background:var(--nav);display:flex;list-style:none}
.nav li{font-size:9.5px;color:#fff;line-height:24px;padding:0 17px}
.nav li.active{background:var(--nav-active);padding:0 14px}
/* gallery */
.photo{background:linear-gradient(160deg,#8aa0b8,#cdd6de 45%,#6d7a5a)}
.hero{left:6px;top:126px;width:444px;height:198px}
/* services */
.services{left:43px;top:340px;width:576px;height:317px;background:var(--panel);border-radius:5px}
.svc{position:absolute;width:110px;text-align:center}
.svc .tile{width:90px;height:90px;margin:0 auto;background:var(--tile);border-radius:5px;display:flex;align-items:center;justify-content:center}
.svc .tile .disc{width:78px;height:78px;background:#fff;border-radius:50%;display:flex;align-items:center;justify-content:center}
.svc p{font-size:11px;line-height:11px;color:#555;margin-top:10px}
/* info columns */
.info{top:678px}
.info h2{font-size:14.5px;font-weight:400;color:var(--blue);line-height:18px;margin-bottom:10px}
.info p,.info li{font-size:7.6px;line-height:11.6px;color:var(--muted);list-style:none;padding-left:6px}
.btn{position:absolute;top:845px;height:22px;background:var(--blue);color:#fff;font-size:9.5px;line-height:22px;padding:0 14px}
.vrule{position:absolute;top:676px;width:1px;height:194px;background:var(--rule)}
.hrule{left:37px;top:890px;width:586px;height:1px;background:var(--rule)}
.accred-title{left:0;top:900px;width:660px;text-align:center;font-size:20px;font-weight:400;color:#333}
.badge{position:absolute;background:#c9d3e3;border-radius:3px}
/* footer */
.footer{left:0;top:1027px;width:660px;height:173px;background:linear-gradient(180deg,#d6d6d6,#ececec 70%,#e2e2e2)}
.fcol{position:absolute;top:16px}
.fcol .main{font-size:11px;line-height:14.5px;color:#444;font-weight:600}
.fcol .sub{font-size:11px;line-height:11.5px;color:#555}
.fcol .link{font-size:7.8px;line-height:11.7px;color:#777}
.follow{font-size:14px;color:#888;margin-top:4px}
.fvrule{position:absolute;top:10px;width:1px;height:150px;background:#bbb}
.social{position:absolute;left:146px;top:124px;width:50px;display:flex;flex-direction:column;align-items:center;gap:2px}
.social .sq{width:24px;height:24px;background:var(--blue)}
.social span{font-size:7px;color:var(--blue)}
.fmap{left:511px;top:80px;width:102px;height:76px;background:linear-gradient(135deg,#cfe0c4,#9fbcd8)}
</style>
</head>
<body>
<div class="backdrop left" role="img" aria-label="Blue perspective grid background"></div>
<div class="backdrop right" role="img" aria-label="Blue perspective grid background"></div>

<div class="page">
  <header>
    <div class="abs brand"><div class="brand-mark"></div><div class="brand-name">Steerwell Driver Training</div></div>
    <div class="abs coverage">
      <div class="title">Training available across NZ</div>
      <div class="map" role="img" aria-label="Map of New Zealand"></div>
      <div class="office"><b>Head Office:</b><br>Harbourside, Eastvale<br>Branches nationwide</div>
    </div>
    <div class="abs tagline">
      <h1>Driver, driving instructor &amp; driver assessor education &amp;training</h1>
      <p>Vehicle types include: heavy vehicles, light fleet vehicles, buses, forklifts and specialist machines<br>
      Registered with NQB and National Road Authority Approved Training Provider<br>
      <em>“Upskilling drivers to be professional, safe and efficient”</em></p>
    </div>
  </header>

  <ul class="abs nav">
    <li class="active">Home</li><li>About</li><li>Courses</li><li>Locations</li><li>Resources</li><li>Links</li><li>FAQs/ Enquiry</li><li>Contact/Map</li>
  </ul>

  <div class="abs photo hero" role="img" aria-label="Driver training tanker truck on a test track"></div>
  <div class="abs photo" style="left:455px;top:126px;width:98px;height:98px" role="img" aria-label="Training truck"></div>
  <div class="abs photo" style="left:556px;top:126px;width:98px;height:98px" role="img" aria-label="Light fleet utility vehicle"></div>
  <div class="abs photo" style="left:455px;top:227px;width:98px;height:97px" role="img" aria-label="Truck with crane"></div>
  <div class="abs photo" style="left:556px;top:227px;width:98px;height:97px" role="img" aria-label="Heavy truck cab"></div>

  <section class="abs services">
    <div class="svc" style="left:11px;top:13px"><div class="tile"><div class="disc"><svg width="50" height="50" viewBox="0 0 50 50"><path d="M8 26l10 12L44 10" fill="none" stroke="#111" stroke-width="8"/></svg></div></div><p>NRA Approved Driver Licence &amp; Endorsement Courses</p></div>
    <div class="svc" style="left:122px;top:13px"><div class="tile"><div class="disc"><svg width="60" height="30" viewBox="0 0 60 30"><rect x="14" y="4" width="44" height="16" fill="#111"/><rect x="2" y="8" width="11" height="12" fill="#111"/><circle cx="8" cy="23" r="4" fill="#111"/><circle cx="40" cy="23" r="4" fill="#111"/><circle cx="50" cy="23" r="4" fill="#111"/></svg></div></div><p>Heavy Vehicle</p></div>
    <div class="svc" style="left:233px;top:13px"><div class="tile"><div class="disc"><svg width="56" height="34" viewBox="0 0 56 34"><rect x="4" y="12" width="48" height="14" rx="3" fill="#111"/><path d="M12 12l6-9h20l6 9z" fill="#111"/><circle cx="15" cy="27" r="5" fill="#111"/><circle cx="41" cy="27" r="5" fill="#111"/></svg></div></div><p>Light Vehicle Fleets</p></div>
    <div class="svc" style="left:344px;top:13px"><div class="tile"><div class="disc"><svg width="50" height="46" viewBox="0 0 50 46"><rect x="6" y="4" width="4" height="38" fill="#111"/><rect x="10" y="36" width="12" height="4" fill="#111"/><rect x="22" y="18" width="22" height="18" fill="#111"/><circle cx="28" cy="38" r="5" fill="#111"/><circle cx="40" cy="38" r="5" fill="#111"/></svg></div></div><p>Forklifts</p></div>
    <div class="svc" style="left:466px;top:13px"><div class="tile"><div class="disc"><svg width="52" height="44" viewBox="0 0 52 44"><path d="M6 30L18 6l12 14" fill="none" stroke="#111" stroke-width="4"/><rect x="26" y="18" width="20" height="14" fill="#111"/><circle cx="30" cy="36" r="5" fill="#111"/><circle cx="44" cy="36" r="5" fill="#111"/></svg></div></div><p>Plant &amp; Telehandler</p></div>

    <div class="svc" style="left:11px;top:164px"><div class="tile"><div class="disc"><svg width="34" height="52" viewBox="0 0 34 52"><rect x="2" y="2" width="30" height="6" fill="#111"/><path d="M4 10l26 10M30 10L4 20M4 20l26 10M30 20L4 30M4 30l26 10M30 30L4 40" stroke="#111" stroke-width="3"/><rect x="2" y="42" width="30" height="8" fill="#111"/></svg></div></div><p>Elevated Work Platforms / Scissor Lifts</p></div>
    <div class="svc" style="left:122px;top:164px"><div class="tile"><div class="disc"><svg width="46" height="38" viewBox="0 0 46 38"><rect x="4" y="4" width="38" height="24" fill="none" stroke="#111" stroke-width="3"/><path d="M14 28v8M32 28v8" stroke="#111" stroke-width="3"/></svg></div></div><p>Driving Instructors &amp; Assessors</p></div>
    <div class="svc" style="left:233px;top:164px"><div class="tile"><div class="disc"><svg width="54" height="34" viewBox="0 0 54 34"><rect x="2" y="4" width="50" height="22" rx="3" fill="none" stroke="#111" stroke-width="3"/><path d="M2 14h50" stroke="#111" stroke-width="2"/><circle cx="13" cy="28" r="4" fill="#111"/><circle cx="41" cy="28" r="4" fill="#111"/></svg></div></div><p>Bus, Coach &amp; Taxi</p></div>
    <div class="svc" style="left:344px;top:164px"><div class="tile"><div class="disc"><svg width="56" height="30" viewBox="0 0 56 30"><rect x="4" y="10" width="48" height="10" fill="#111"/><path d="M20 10l4-8h8" stroke="#111" stroke-width="3" fill="none"/><circle cx="14" cy="22" r="6" fill="#111"/><circle cx="42" cy="22" r="6" fill="#111"/></svg></div></div><p>Four Wheel Drive &amp; Quads</p></div>
    <div class="svc" style="left:466px;top:164px"><div class="tile"><div class="disc"><svg width="60" height="60" viewBox="0 0 60 60"><rect x="12" y="12" width="36" height="36" transform="rotate(45 30 30)" fill="#222"/><rect x="10" y="26" width="40" height="8" fill="#fff"/></svg></div></div><p>HazGoods Approved Handler / Filler Dangerous Goods Handling</p></div>
  </section>

  <div class="abs info" style="left:43px;width:176px">
    <h2>Steerwell is<br>registered with</h2>
    <ul>
      <li>- NQB as a PTE (Private Training Establishment)</li>
      <li>- National Road Authority for approved licence courses</li>
      <li>- Skillforge ITO/ SafeWork Agency for forklift training</li>
      <li>- Hazard Standards Office for HazGoods Certification</li>
      <li>- Department of Roads / National Road Authority for SAFEDRIVE driver &amp; instructor courses</li>
    </ul>
  </div>
  <div class="vrule" style="left:230px"></div>
  <div class="abs info" style="left:242px;width:194px">
    <h2>Steerwell Courses<br>FAQs</h2>
    <p style="padding-left:0">Find out the answers to the most often asked questions about Steerwell courses here...</p>
    <ul>
      <li>- Does Steerwell run courses in my location?</li>
      <li>- Do you have advanced driving courses?</li>
      <li>- What accreditation will your (course name) give me?</li>
      <li>- How much does the course I want to do cost?</li>
    </ul>
  </div>
  <div class="vrule" style="left:445px"></div>
  <div class="abs info" style="left:454px;width:160px">
    <h2>Steerwell Courses<br>by Location</h2>
    <ul>
      <li>- Steerwell run courses throughout New Zealand.</li>
      <li>- You can find courses by location and enrol online.</li>
      <li>- If you can't find the course you want in your area, please contact us as we can run any course in any location (conditions may apply).</li>
    </ul>
  </div>
  <div class="btn" style="left:43px">Find out more</div>
  <div class="btn" style="left:242px">Find out more</div>
  <div class="btn" style="left:455px">Browse courses by location</div>

  <div class="abs hrule"></div>
  <h2 class="abs accred-title">Accreditations &amp;Affiliations</h2>
  <div class="badge" style="left:37px;top:937px;width:62px;height:24px"></div>
  <div class="badge" style="left:107px;top:937px;width:100px;height:24px"></div>
  <div class="badge" style="left:212px;top:935px;width:75px;height:28px"></div>
  <div class="badge" style="left:290px;top:937px;width:80px;height:24px;background:#555"></div>
  <div class="badge" style="left:377px;top:937px;width:72px;height:24px"></div>
  <div class="badge" style="left:452px;top:937px;width:68px;height:24px"></div>
  <div class="badge" style="left:530px;top:935px;width:80px;height:24px"></div>
  <div class="badge" style="left:148px;top:978px;width:76px;height:32px"></div>
  <div class="badge" style="left:232px;top:978px;width:44px;height:34px"></div>
  <div class="badge" style="left:290px;top:982px;width:106px;height:26px"></div>
  <div class="badge" style="left:412px;top:975px;width:116px;height:37px;background:#222"></div>

  <footer class="abs footer">
    <div class="fcol" style="left:22px">
      <div class="main">Home<br>About</div>
      <div class="sub">- Company accreditations<br>- Instructors/assessors<br>- Management admin<br>- Testimonials</div>
      <div class="main" style="margin-top:6px">Course Locations</div>
      <div class="follow">Follow On</div>
      <div class="link">Follow us for the latest world<br>of work insights and news.</div>
    </div>
    <div class="social"><div class="sq"></div><span>Socialsphere</span></div>
    <div class="fvrule" style="left:208px"></div>
    <div class="fcol" style="left:216px">
      <div class="main">Courses</div>
      <div class="link">- NRA Approved Driver Licence &amp; Endorsement Courses<br>- Heavy Vehicle<br>- Light Vehicle Fleets<br>- Forklifts<br>- Plant &amp; Telehandler<br>- Elevated Work Platforms / Scissor Lifts<br>- Driving Instructors &amp; Assessors<br>- Bus, Coach &amp; Taxi<br>- Four Wheel Drive &amp; Quads<br>- HazGoods Approved Handler / Filler – Dangerous Goods Handling</div>
    </div>
    <div class="fvrule" style="left:490px"></div>
    <div class="fcol" style="left:509px">
      <div class="main">Resources<br>Links<br>FAQs/ Enquiry<br>Contact/Map</div>
    </div>
    <div class="abs fmap" role="img" aria-label="Location map of head office"></div>
  </footer>
</div>
</body>
</html>
```